Word Template for official reports

I would like to Word template to use for a research project. The key topic of the research project is: A cyber security toolkit to protect the privacy data/infrastructure of the health care industry.This file will be used by the entire research team (approx. 50 people) to describe the project outcomes and provide that to the Halvard Governing Panel. Therefore, the design should be professional, and official. The fact that the word file will be used by several people for the same project means that the template should allow the user any time (s)he adds a table to have a particular format. Any time the user adds bullet points, these should have a particular colour and shape, and so on. The users have MS windows and MAC. About the word design, you should use the project logo that I am attaching and of course you may use at the layout colors that matches to this logo. Pay attention, we need to keep the file size as low as possible so please avoid adding graphics on each page. Graphics at the cover page are enough. Regarding its structure, I am attaching the basic word (non-professional), without design. You may notice at the bottom of each slide there is the OV flag and a particular phrase beside. Please use that in your proposal as well. You may find images for the OV flag here: https://ovarnet.example/ovar-league/about-ov/symbols/flag_en If you need any further clarifications, please do not hesitate to contact me.

```html
<!DOCTYPE html>
<html lang="en">
<head>
<meta charset="utf-8">
<title>Veltrix report template – page set</title>
<link href="https://fonts.googleapis.com/css2?family=Lato:ital,wght@0,400;0,700;1,400&display=swap" rel="stylesheet">
<style>
:root{
  --stage:#3a3a3a;
  --paper:#ffffff;
  --teal:#1aab9b;
  --teal-mid:#5fcfc4;
  --teal-light:#a9e7e1;
  --ink:#4a4a4a;
  --ink-soft:#777777;
  --rule:#bbbbbb;
  --band:#e4e4e4;
  --panel:#efefef;
  --flag:#1d3f9a;
  --dark:#333333;
}
*{box-sizing:border-box;margin:0;padding:0}
html,body{width:871px;height:1200px;overflow:hidden;background:var(--stage)}
body{position:relative;font-family:'Lato',sans-serif;color:var(--ink)}
.page{position:absolute;width:405px;height:573px;background:var(--paper);overflow:hidden}
.page--cover{left:22px;top:22px}
.page--text{left:440px;top:22px}
.page--tables{left:22px;top:607px}
.page--charts{left:440px;top:607px}
.running-head{position:absolute;left:50px;top:25px;font-size:4.6px;color:var(--ink-soft)}
.brand{position:absolute;right:9px;top:11px;display:flex;align-items:center;gap:4px;color:var(--teal);font-size:17px;font-weight:400;letter-spacing:.5px}
.brand__dot{width:20px;height:20px;border:2.5px solid var(--teal);border-radius:50%}
.cover-band{position:absolute;left:0;top:46px;width:405px;height:115px;background:linear-gradient(120deg,#159e8f,#2bbfae 55%,#1aa898)}
.cover-title{position:absolute;left:50px;top:180px;font-size:15.5px;font-weight:700;color:var(--teal)}
.cover-subtitle{position:absolute;left:50px;top:203px;font-size:9.5px;color:var(--ink)}
.heading{position:absolute;left:50px;font-size:7.4px;font-weight:700;color:var(--teal)}
.copy{position:absolute;font-size:6px;line-height:8.1px;color:var(--ink);overflow:hidden}
.copy p+p{margin-top:8px}
.copy--wide{left:50px;width:305px}
.copy--left{left:50px;width:141px;top:270px;height:252px}
.copy--right{left:212px;width:143px;top:270px;height:252px}
.copy--accent{color:var(--teal);font-style:italic}
.footer{position:absolute;left:0;bottom:0;width:405px;height:36px;background:var(--band);display:flex;align-items:center;gap:6px;padding-left:4px}
.footer__flag{width:36px;height:25px;background:var(--flag);flex:none}
.footer__text{font-size:6.3px;line-height:9.6px;color:var(--ink);width:330px}
.data-table{position:absolute;left:50px;width:306px;border-collapse:collapse;font-size:4.8px;color:var(--ink)}
.data-table th,.data-table td{height:13px;padding:0 4px;text-align:right;font-weight:400}
.data-table th:first-child,.data-table td:first-child{text-align:left;width:96px}
.data-table tr+tr td{border-top:.6px solid #d5d5d5}
.data-table--rules thead th{border-top:1px solid var(--dark);border-bottom:.6px solid var(--rule);color:var(--ink-soft)}
.data-table--rules tbody tr:last-child td{border-bottom:1px solid var(--dark)}
.data-table--teal{border:1px solid var(--teal)}
.data-table--teal thead th{background:var(--teal);color:#fff}
.data-table--grey{border:1px solid var(--rule)}
.data-table--grey thead th{background:#dcdcdc}
.data-table--dark{border:1px solid var(--dark)}
.data-table--dark thead th{background:var(--dark);color:#fff;font-weight:700}
.chart{position:absolute;left:40px;width:320px;height:80px;font-family:'Lato',sans-serif}
.chart text{font-size:4.8px;fill:var(--ink-soft)}
.info-panel{position:absolute;left:0;top:333px;width:405px;height:204px;background:var(--panel)}
.contact{position:absolute;left:50px;top:490px;font-size:5.5px;line-height:7.5px}
</style>
</head>
<body>

<section class="page page--cover">
  <div class="running-head">Lorem ipsum dolor sit amet</div>
  <div class="brand"><span class="brand__dot"></span>VELTRIX</div>
  <div class="cover-band" role="img" aria-label="Cover artwork: teal network of connected nodes with padlock icons"></div>
  <h1 class="cover-title">Project title goes here</h1>
  <div class="cover-subtitle">Project subtitle goes here</div>
  <h2 class="heading" style="top:254px">Lorem ipsum dolor sit amet</h2>
  <div class="copy copy--left">
    <p>Lorem ipsum dolor sit amet, consectetur adipiscing elit, sed do eiusmod tempor incididunt ut labore et dolore magna aliqua. Ut enim ad minim veniam, quis nostrud exercitation ullamco laboris nisi ut aliquip ex ea commodo consequat. Duis aute irure dolor in reprehenderit in voluptate velit esse cillum dolore eu fugiat nulla pariatur. Excepteur sint occaecat cupidatat non proident, sunt in culpa qui officia deserunt mollit anim id est laborum.</p>
    <p>Sed ut perspiciatis unde omnis iste natus error sit voluptatem accusantium doloremque laudantium, totam rem aperiam, eaque ipsa quae ab illo inventore veritatis et quasi architecto beatae vitae dicta sunt explicabo. Nemo enim ipsam voluptatem quia voluptas sit aspernatur aut odit aut fugit, sed quia consequuntur magni dolores eos qui ratione voluptatem sequi nesciunt. Neque porro quisquam est, qui dolorem ipsum quia dolor sit amet, consectetur, adipisci velit, sed quia non numquam eius modi tempora incidunt ut labore et dolore magnam aliquam quaerat voluptatem. Ut enim ad minima veniam, quis nostrum exercitationem ullam corporis suscipit laboriosam, nisi ut aliquid ex ea commodi consequatur? Quis autem vel eum iure reprehenderit qui in ea voluptate velit esse quam nihil molestiae consequatur, vel illum qui dolorem eum fugiat quo voluptas nulla pariatur?</p>
  </div>
  <div class="copy copy--right">
    <p>At vero eos et accusamus et iusto odio dignissimos ducimus qui blanditiis praesentium voluptatum deleniti atque corrupti quos dolores et quas molestias excepturi sint occaecati cupiditate non provident, similique sunt in culpa qui officia deserunt mollitia animi, id est laborum et dolorum fuga. Et harum quidem rerum facilis est et expedita distinctio. Nam libero tempore, cum soluta nobis est eligendi optio cumque nihil impedit quo minus id quod maxime placeat facere possimus, omnis voluptas assumenda est, omnis dolor repellendus. Temporibus autem quibusdam et aut officiis debitis aut rerum necessitatibus saepe eveniet ut et voluptates repudiandae sint et molestiae non recusandae. Itaque earum rerum hic tenetur a sapiente delectus, ut aut reiciendis voluptatibus maiores alias consequatur aut perferendis doloribus asperiores repellat.</p>
    <p>Lorem ipsum dolor sit amet, consectetur adipiscing elit, sed do eiusmod tempor incididunt ut labore et dolore magna aliqua. Ut enim ad minim veniam, quis nostrud exercitation ullamco laboris nisi ut aliquip ex ea commodo consequat. Duis aute irure dolor in reprehenderit in voluptate velit esse cillum dolore eu fugiat nulla pariatur. Excepteur sint occaecat cupidatat non proident, sunt in culpa qui officia deserunt mollit anim id est laborum.</p>
  </div>
  <footer class="footer"><div class="footer__flag"></div><p class="footer__text">This project has received funding from the Ovar League's Meridian 2030 research and innovation program me under grant agreement &nbsp;No 904417 Connected Care, Data Trust &amp; Resilient Digital Health Systems</p></footer>
</section>

<section class="page page--text">
  <div class="running-head">Lorem ipsum dolor sit amet</div>
  <div class="brand"><span class="brand__dot"></span>VELTRIX</div>
  <h2 class="heading" style="top:49px">Lorem ipsum dolor sit amet</h2>
  <div class="copy copy--wide" style="top:64px;height:42px"><p>Lorem ipsum dolor sit amet, consectetur adipiscing elit, sed do eiusmod tempor incididunt ut labore et dolore magna aliqua. Ut enim ad minim veniam, quis nostrud exercitation ullamco laboris nisi ut aliquip ex ea commodo consequat. Duis aute irure dolor in reprehenderit in voluptate velit esse cillum dolore eu fugiat nulla pariatur. Excepteur sint occaecat cupidatat non proident, sunt in culpa qui officia deserunt mollit anim id est laborum</p></div>
  <div class="copy copy--wide" style="top:113px;height:74px"><p>Sed ut perspiciatis unde omnis iste natus error sit voluptatem accusantium doloremque laudantium, totam rem aperiam, eaque ipsa quae ab illo inventore veritatis et quasi architecto beatae vitae dicta sunt explicabo. Nemo enim ipsam voluptatem quia voluptas sit aspernatur aut odit aut fugit, sed quia consequuntur magni dolores eos qui ratione voluptatem sequi nesciunt. Neque porro quisquam est, qui dolorem ipsum quia dolor sit amet, consectetur, adipisci velit, sed quia non numquam eius modi tempora incidunt ut labore et dolore magnam aliquam quaerat voluptatem. Ut enim ad minima veniam, quis nostrum exercitationem ullam corporis suscipit laboriosam, nisi ut aliquid ex ea commodi consequatur? Quis autem vel eum iure reprehenderit qui in ea voluptate velit esse quam nihil molestiae consequatur, vel illum qui dolorem eum fugiat quo voluptas nulla pariatur?</p></div>
  <div class="copy copy--wide copy--accent" style="top:195px;height:42px"><p>Lorem ipsum dolor sit amet, consectetur adipiscing elit, sed do eiusmod tempor incididunt ut labore et dolore magna aliqua. Ut enim ad minim veniam, quis nostrud exercitation ullamco laboris nisi ut aliquip ex ea commodo consequat. Duis aute irure dolor in reprehenderit in voluptate velit esse cillum dolore eu fugiat nulla pariatur. Excepteur sint occaecat cupidatat non proident, sunt in culpa qui officia deserunt mollit anim id est laborum</p></div>
  <h2 class="heading" style="top:254px">Lorem ipsum dolor sit amet</h2>
  <div class="copy copy--left">
    <p>Lorem ipsum dolor sit amet, consectetur adipiscing elit, sed do eiusmod tempor incididunt ut labore et dolore magna aliqua. Ut enim ad minim veniam, quis nostrud exercitation ullamco laboris nisi ut aliquip ex ea commodo consequat. Duis aute irure dolor in reprehenderit in voluptate velit esse cillum dolore eu fugiat nulla pariatur. Excepteur sint occaecat cupidatat non proident, sunt in culpa qui officia deserunt mollit anim id est laborum.</p>
    <p>Sed ut perspiciatis unde omnis iste natus error sit voluptatem accusantium doloremque laudantium, totam rem aperiam, eaque ipsa quae ab illo inventore veritatis et quasi architecto beatae vitae dicta sunt explicabo. Nemo enim ipsam voluptatem quia voluptas sit aspernatur aut odit aut fugit, sed quia consequuntur magni dolores eos qui ratione voluptatem sequi nesciunt. Neque porro quisquam est, qui dolorem ipsum quia dolor sit amet, consectetur, adipisci velit, sed quia non numquam eius modi tempora incidunt ut labore et dolore magnam aliquam quaerat voluptatem. Ut enim ad minima veniam, quis nostrum exercitationem ullam corporis suscipit laboriosam, nisi ut aliquid ex ea commodi consequatur? Quis autem vel eum iure reprehenderit qui in ea voluptate velit esse quam nihil molestiae consequatur, vel illum qui dolorem eum fugiat quo voluptas nulla pariatur?</p>
  </div>
  <div class="copy copy--right">
    <p>At vero eos et accusamus et iusto odio dignissimos ducimus qui blanditiis praesentium voluptatum deleniti atque corrupti quos dolores et quas molestias excepturi sint occaecati cupiditate non provident, similique sunt in culpa qui officia deserunt mollitia animi, id est laborum et dolorum fuga. Et harum quidem rerum facilis est et expedita distinctio. Nam libero tempore, cum soluta nobis est eligendi optio cumque nihil impedit quo minus id quod maxime placeat facere possimus, omnis voluptas assumenda est, omnis dolor repellendus. Temporibus autem quibusdam et aut officiis debitis aut rerum necessitatibus saepe eveniet ut et voluptates repudiandae sint et molestiae non recusandae. Itaque earum rerum hic tenetur a sapiente delectus, ut aut reiciendis voluptatibus maiores alias consequatur aut perferendis doloribus asperiores repellat.</p>
    <p>Lorem ipsum dolor sit amet, consectetur adipiscing elit, sed do eiusmod tempor incididunt ut labore et dolore magna aliqua. Ut enim ad minim veniam, quis nostrud exercitation ullamco laboris nisi ut aliquip ex ea commodo consequat. Duis aute irure dolor in reprehenderit in voluptate velit esse cillum dolore eu fugiat nulla pariatur. Excepteur sint occaecat cupidatat non proident, sunt in culpa qui officia deserunt mollit anim id est laborum.</p>
  </div>
  <footer class="footer"><div class="footer__flag"></div><p class="footer__text">This project has received funding from the Ovar League's Meridian 2030 research and innovation program me under grant agreement &nbsp;No 904417 Connected Care, Data Trust &amp; Resilient Digital Health Systems</p></footer>
</section>

<section class="page page--tables">
  <div class="running-head">Lorem ipsum dolor sit amet</div>
  <div class="brand"><span class="brand__dot"></span>VELTRIX</div>
  <h2 class="heading" style="top:49px">Lorem ipsum dolor sit amet</h2>
  <div class="copy copy--wide" style="top:64px;height:42px"><p>Lorem ipsum dolor sit amet, consectetur adipiscing elit, sed do eiusmod tempor incididunt ut labore et dolore magna aliqua. Ut enim ad minim veniam, quis nostrud exercitation ullamco laboris nisi ut aliquip ex ea commodo consequat. Duis aute irure dolor in reprehenderit in voluptate velit esse cillum dolore eu fugiat nulla pariatur. Excepteur sint occaecat cupidatat non proident, sunt in culpa qui officia deserunt mollit anim id est laborum</p></div>

  <h3 class="heading" style="top:126px">Table style 1</h3>
  <table class="data-table data-table--rules" style="top:144px">
    <thead><tr><th>Title 1</th><th>Title 2</th><th>Title 3</th><th>Title 4</th><th>Title 5</th></tr></thead>
    <tbody>
      <tr><td>Lorem ipsum</td><td>456</td><td>57</td><td>46</td><td>213</td></tr>
      <tr><td>Lorem ipsum</td><td>356</td><td>4,548</td><td>454</td><td>34</td></tr>
      <tr><td>Lorem ipsum</td><td>54</td><td>5,645</td><td>80</td><td>57</td></tr>
      <tr><td>Lorem ipsum</td><td>23</td><td>65</td><td>-</td><td>233</td></tr>
    </tbody>
  </table>

  <h3 class="heading" style="top:229px">Table style 2</h3>
  <table class="data-table data-table--teal" style="top:247px">
    <thead><tr><th>Title 1</th><th>Title 2</th><th>Title 3</th><th>Title 4</th><th>Title 5</th></tr></thead>
    <tbody>
      <tr><td>Lorem ipsum</td><td>456</td><td>57</td><td>46</td><td>213</td></tr>
      <tr><td>Lorem ipsum</td><td>356</td><td>4,548</td><td>454</td><td>34</td></tr>
      <tr><td>Lorem ipsum</td><td>54</td><td>5,645</td><td>80</td><td>57</td></tr>
      <tr><td>Lorem ipsum</td><td>23</td><td>65</td><td>-</td><td>233</td></tr>
    </tbody>
  </table>

  <h3 class="heading" style="top:333px">Table style 3</h3>
  <table class="data-table data-table--grey" style="top:352px">
    <thead><tr><th>Title 1</th><th>Title 2</th><th>Title 3</th><th>Title 4</th><th>Title 5</th></tr></thead>
    <tbody>
      <tr><td>Lorem ipsum</td><td>456</td><td>57</td><td>46</td><td>213</td></tr>
      <tr><td>Lorem ipsum</td><td>356</td><td>4,548</td><td>454</td><td>34</td></tr>
      <tr><td>Lorem ipsum</td><td>54</td><td>5,645</td><td>80</td><td>57</td></tr>
      <tr><td>Lorem ipsum</td><td>23</td><td>65</td><td>-</td><td>233</td></tr>
    </tbody>
  </table>

  <h3 class="heading" style="top:436px">Table style 4</h3>
  <table class="data-table data-table--dark" style="top:455px">
    <thead><tr><th>Title 1</th><th>Title 2</th><th>Title 3</th><th>Title 4</th><th>Title 5</th></tr></thead>
    <tbody>
      <tr><td>Lorem ipsum</td><td>456</td><td>57</td><td>46</td><td>213</td></tr>
      <tr><td>Lorem ipsum</td><td>356</td><td>4,548</td><td>454</td><td>34</td></tr>
      <tr><td>Lorem ipsum</td><td>54</td><td>5,645</td><td>80</td><td>57</td></tr>
      <tr><td>Lorem ipsum</td><td>23</td><td>65</td><td>-</td><td>233</td></tr>
    </tbody>
  </table>
  <footer class="footer"><div class="footer__flag"></div><p class="footer__text">This project has received funding from the Ovar League's Meridian 2030 research and innovation program me under grant agreement &nbsp;No 904417 Connected Care, Data Trust &amp; Resilient Digital Health Systems</p></footer>
</section>

<section class="page page--charts">
  <div class="running-head">Lorem ipsum dolor sit amet</div>
  <div class="brand"><span class="brand__dot"></span>VELTRIX</div>
  <h2 class="heading" style="top:49px">Lorem ipsum dolor sit amet</h2>
  <div class="copy copy--wide" style="top:64px;height:42px"><p>Lorem ipsum dolor sit amet, consectetur adipiscing elit, sed do eiusmod tempor incididunt ut labore et dolore magna aliqua. Ut enim ad minim veniam, quis nostrud exercitation ullamco laboris nisi ut aliquip ex ea commodo consequat. Duis aute irure dolor in reprehenderit in voluptate velit esse cillum dolore eu fugiat nulla pariatur. Excepteur sint occaecat cupidatat non proident, sunt in culpa qui officia deserunt mollit anim id est laborum</p></div>

  <h3 class="heading" style="top:126px">Chart style 1</h3>
  <svg class="chart" style="top:140px" viewBox="0 0 320 80" aria-label="Clustered bar chart, three series across four categories">
    <text x="8" y="10">10</text><text x="10" y="30">5</text><text x="10" y="50">0</text>
    <line x1="24" y1="48" x2="312" y2="48" stroke="#cccccc" stroke-width=".6"/>
    <g fill="#1aab9b"><rect x="38" y="30.8" width="12" height="17.2"/><rect x="113" y="38" width="12" height="10"/><rect x="184" y="34" width="12" height="14"/><rect x="259" y="30" width="12" height="18"/></g>
    <g fill="#5fcfc4"><rect x="51" y="38.4" width="12" height="9.6"/><rect x="126" y="30.4" width="12" height="17.6"/><rect x="197" y="40.8" width="12" height="7.2"/><rect x="272" y="36.8" width="12" height="11.2"/></g>
    <g fill="#a9e7e1"><rect x="64" y="40" width="12" height="8"/><rect x="139" y="40.8" width="12" height="7.2"/><rect x="210" y="36.8" width="12" height="11.2"/><rect x="285" y="28" width="12" height="20"/></g>
    <text x="47" y="59">Category 1</text><text x="122" y="59">Category 2</text><text x="193" y="59">Category 3</text><text x="268" y="59">Category 4</text>
    <rect x="88" y="64.5" width="3" height="3" fill="#1aab9b"/><text x="93" y="67.5">Series 1</text>
    <rect x="168" y="64.5" width="3" height="3" fill="#5fcfc4"/><text x="173" y="67.5">Series 2</text>
    <rect x="248" y="64.5" width="3" height="3" fill="#a9e7e1"/><text x="253" y="67.5">Series 3</text>
  </svg>

  <h3 class="heading" style="top:229px">Chart style 2</h3>
  <svg class="chart" style="top:245px" viewBox="0 0 320 80" aria-label="Stacked bar chart, three series across four categories">
    <text x="8" y="10">20</text><text x="8" y="30">10</text><text x="10" y="50">0</text>
    <line x1="24" y1="48" x2="312" y2="48" stroke="#cccccc" stroke-width=".6"/>
    <g fill="#1aab9b"><rect x="41" y="39.4" width="30" height="8.6"/><rect x="116" y="43" width="30" height="5"/><rect x="187" y="41" width="30" height="7"/><rect x="262" y="39" width="30" height="9"/></g>
    <g fill="#5fcfc4"><rect x="41" y="34.6" width="30" height="4.8"/><rect x="116" y="34.2" width="30" height="8.8"/><rect x="187" y="37.4" width="30" height="3.6"/><rect x="262" y="33.4" width="30" height="5.6"/></g>
    <g fill="#a9e7e1"><rect x="41" y="30.6" width="30" height="4"/><rect x="116" y="30.6" width="30" height="3.6"/><rect x="187" y="31.8" width="30" height="5.6"/><rect x="262" y="23.4" width="30" height="10"/></g>
    <text x="47" y="59">Category 1</text><text x="122" y="59">Category 2</text><text x="193" y="59">Category 3</text><text x="268" y="59">Category 4</text>
    <rect x="88" y="64.5" width="3" height="3" fill="#1aab9b"/><text x="93" y="67.5">Series 1</text>
    <rect x="168" y="64.5" width="3" height="3" fill="#5fcfc4"/><text x="173" y="67.5">Series 2</text>
    <rect x="248" y="64.5" width="3" height="3" fill="#a9e7e1"/><text x="253" y="67.5">Series 3</text>
  </svg>

  <div class="info-panel"></div>
  <h2 class="heading" style="top:343px">Important Informations</h2>
  <div class="copy copy--wide" style="top:357px;height:42px"><p>Lorem ipsum dolor sit amet, consectetur adipiscing elit, sed do eiusmod tempor incididunt ut labore et dolore magna aliqua. Ut enim ad minim veniam, quis nostrud exercitation ullamco laboris nisi ut aliquip ex ea commodo consequat. Duis aute irure dolor in reprehenderit in voluptate velit esse cillum dolore eu fugiat nulla pariatur. Excepteur sint occaecat cupidatat non proident, sunt in culpa qui officia deserunt mollit anim id est laborum</p></div>
  <div class="copy copy--wide" style="top:406px;height:50px"><p>Sed ut perspiciatis unde omnis iste natus error sit voluptatem accusantium doloremque laudantium, totam rem aperiam, eaque ipsa quae ab illo inventore veritatis et quasi architecto beatae vitae dicta sunt explicabo. Nemo enim ipsam voluptatem quia voluptas sit aspernatur aut odit aut fugit, sed quia consequuntur magni dolores eos qui ratione voluptatem sequi nesciunt. Neque porro quisquam est, qui dolorem ipsum quia dolor sit amet, consectetur, adipisci velit, sed quia non numquam eius modi tempora incidunt ut labore et dolore magnam aliquam quaerat voluptatem.</p></div>
  <h2 class="heading" style="top:473px">Contact details</h2>
  <div class="contact">
    Phone: xxx.xxx.xxx<br>
    Address: xxx, Lorem Ipsum, Lorem<br>
    Email: lorem@example.com<br>
    Website: www.example.com
  </div>
  <footer class="footer"><div class="footer__flag"></div><p class="footer__text">This project has received funding from the Ovar League's Meridian 2030 research and innovation program me under grant agreement &nbsp;No 904417 Connected Care, Data Trust &amp; Resilient Digital Health Systems</p></footer>
</section>

</body>
</html>
```